Wine Labels for new product to attract Millenial consumers

SipRoam Design Brief
1. Intro:
Marrabel Cellars is a 120 year old family owned Australian wine company renowned for producing traditional premium quality wines. This project is aimed at breaking through this perception of Marrabel to show main stream Australian retailers that we can be innovative and relevant and that we know who their millennial shoppers are and we know how to attract their attention. This needs to be achieved through the combination of innovative and clever design paired with a product that challenges conventional Australian wine philosophies and appeals to those wine drinkers seeking authentic and alternative wine experiences.
2. Feelings:
This new wine should evoke a new set of feelings in retailers that they don’t usually associate with Marrabel Cellars. Retailers should feel excited, challenged and impressed by our knowledge of the millennial demographic. The packaging should make the shopper feel surprised, curious, cool, aspirational, understood, adventurous, individual, fashionable, progressive and engaged. It also needs to evoke a sense of the occasion it should be consumed in, with food and friends in a fun environment and evoke a sense of conviviality and a desire for shared social interaction.
3. Look + Feel:
It shouldn’t look or feel like anything Marrabel Cellars is known for and has done before. It should not carry our branding or logo, this should be a standalone product range. It should feel modern, cool, clever and hip. It should feel real, authentic, artisanal and most of all it should challenge the traditional visual discourse of wine as bored, tired, stiff and conservative. The design should be respected piece of art in its own right. It should make the shopper feel like getting a few friends around for dinner and drinks.
4. Brand Position:
This product range needs to challenge the existing brand positioning of Marrabel Cellars. It should clearly target the millennial demographic and the hipster sub culture who are being lured into new alcohol categories by cool design and positioning. “Exposed to a barrage of drinks offerings, the report found that wine is in danger of losing Generation Y to other more engaging drinks categories such as beer, cider and spirits ……. With 18-25 year olds accounting for 25% of the wine drinking population, Millennials represent an important sector of the wine market, thus keeping their attention and interest should remain a priority for wine brands.” Grape Insight Review. “…. Wine is becoming increasingly cool with the influencers and trend setters of a whole new generation.” Pour Journal.
5. Needs:
2 wine labels, one white and one red, but linked by design. Should fit a 500 ml glass bottle and design should be able to carry over to some innovative packaging into small lots of 4 or 6 like beer. For the purpose of design use the name SipRoam White and SipRoam Red. Relating the wine to food and how it should be consumed is important as this needs to be seen as a lifestyle accessory to food to combat the anti-alcohol lobby and the socially acceptable practise of eating and drinking together as part of a social experience. An area for approximately 200 words of mandatory information and declarations needs to be provided.

https://www.examplepins.test/MarrabelCellars/siproam-moodboard/

Full brief in project description

Requirements
Must have
• Full brief in project description
Nice to have
Should not have

```html
<!DOCTYPE html>
<html lang="en">
<head>
<meta charset="utf-8">
<title>SipRoam White and SipRoam Red Labels</title>
<link rel="stylesheet" href="https://fonts.googleapis.com/css2?family=Arvo:wght@700&family=Bebas+Neue&display=swap">
<style>
  :root {
    --page: #ffffff;
    --white-label-bg: #6f6b6a;
    --white-label-pattern: #5d5958;
    --white-ink: #ffffff;
    --white-shade: #9c9897;
    --red-label-bg: #302e2e;
    --red-label-pattern: #222020;
    --red-ink: #f2525a;
    --red-shade: #8c3237;
  }
  html, body {
    margin: 0;
    width: 1200px;
    height: 641px;
    overflow: hidden;
    background: var(--page);
  }
  .label-range {
    position: relative;
    width: 1200px;
    height: 641px;
    display: flex;
    justify-content: center;
    align-items: center;
    gap: 120px;
  }
  .wine-label {
    width: 346px;
    height: 641px;
    display: block;
  }
  .word-big {
    font-family: "Bebas Neue", "Oswald", sans-serif;
    font-size: 190px;
  }
  .word-variety,
  .label-facts {
    font-family: "Arvo", "Roboto Slab", serif;
    font-weight: 700;
  }
  .word-variety { font-size: 44px; }
  .label-facts { font-size: 29px; }

  .wine-label--white .label-base { fill: var(--white-label-bg); }
  .wine-label--white .label-pattern-tone { stop-color: var(--white-label-pattern); }
  .wine-label--white .ink { fill: var(--white-ink); }
  .wine-label--white .rule { stroke: var(--white-ink); }
  .wine-label--white .shade { fill: var(--white-shade); }

  .wine-label--red .label-base { fill: var(--red-label-bg); }
  .wine-label--red .label-pattern-tone { stop-color: var(--red-label-pattern); }
  .wine-label--red .ink { fill: var(--red-ink); }
  .wine-label--red .rule { stroke: var(--red-ink); }
  .wine-label--red .shade { fill: var(--red-shade); }
</style>
</head>
<body>
<main class="label-range">

  <svg class="wine-label wine-label--white" viewBox="0 0 346 641" aria-label="SipRoam White label">
    <defs>
      <radialGradient id="white-pattern-glow" cx="50%" cy="50%" r="70%">
        <stop offset="0" class="label-pattern-tone" stop-opacity="0"/>
        <stop offset="1" class="label-pattern-tone" stop-opacity="0.8"/>
      </radialGradient>
    </defs>
    <rect class="label-base" width="346" height="641"/>
    <rect role="img" aria-label="Pattern of food and tableware icons: plates, fish, bread, cutlery, fruit and leaves" width="346" height="641" fill="url(#white-pattern-glow)"/>

    <text class="word-big shade" x="31" y="204" textLength="294" lengthAdjust="spacingAndGlyphs">SIP</text>
    <text class="word-big ink" x="25" y="198" textLength="294" lengthAdjust="spacingAndGlyphs">SIP</text>

    <line class="rule" x1="28" y1="257" x2="88" y2="257" stroke-width="6"/>
    <text class="word-variety ink" x="173" y="270" text-anchor="middle">white</text>
    <line class="rule" x1="258" y1="257" x2="320" y2="257" stroke-width="6"/>

    <text class="word-big shade" x="29" y="513" textLength="298" lengthAdjust="spacingAndGlyphs">ROAM</text>
    <text class="word-big ink" x="23" y="507" textLength="298" lengthAdjust="spacingAndGlyphs">ROAM</text>

    <text class="label-facts ink" x="28" y="593">13% vol.</text>
    <text class="label-facts ink" x="322" y="593" text-anchor="end">500 ml</text>
  </svg>

  <svg class="wine-label wine-label--red" viewBox="0 0 346 641" aria-label="SipRoam Red label">
    <defs>
      <radialGradient id="red-pattern-glow" cx="50%" cy="50%" r="70%">
        <stop offset="0" class="label-pattern-tone" stop-opacity="0"/>
        <stop offset="1" class="label-pattern-tone" stop-opacity="0.8"/>
      </radialGradient>
    </defs>
    <rect class="label-base" width="346" height="641"/>
    <rect role="img" aria-label="Pattern of food and tableware icons: plates, fish, bread, cutlery, fruit and leaves" width="346" height="641" fill="url(#red-pattern-glow)"/>

    <text class="word-big shade" x="31" y="204" textLength="294" lengthAdjust="spacingAndGlyphs">SIP</text>
    <text class="word-big ink" x="25" y="198" textLength="294" lengthAdjust="spacingAndGlyphs">SIP</text>

    <line class="rule" x1="20" y1="257" x2="108" y2="257" stroke-width="6"/>
    <text class="word-variety ink" x="173" y="270" text-anchor="middle">red</text>
    <line class="rule" x1="238" y1="257" x2="326" y2="257" stroke-width="6"/>

    <text class="word-big shade" x="29" y="513" textLength="298" lengthAdjust="spacingAndGlyphs">ROAM</text>
    <text class="word-big ink" x="23" y="507" textLength="298" lengthAdjust="spacingAndGlyphs">ROAM</text>

    <text class="label-facts ink" x="18" y="593">13% vol.</text>
    <text class="label-facts ink" x="330" y="593" text-anchor="end">500 ml</text>
  </svg>

</main>
</body>
</html>
```